A modern web page for a software product

We need a web page for a software product, which is an advanced solution based on Machine Learning and Natural Language processing. We already have a logo of the product and expect the web page to be inline with the logo colors. The design should be for one page web site with scrolled sections - details of the content and guidelines in the attachments.

Target Market(s)

software company

Industry/Entity Type

It Company

Number of Pages Required

1 page

Colors

Designer to choose colors to be used in the design.

Requirements
Must have
• - modern icons and graphics
• - inline with the logo colors
• - be related to Machine Learining, AI, data processing
• - should have two language versions: english and polish both are attached.
Nice to have
• - animation/motion
Should not have
• - any photos embedded

```html
<!DOCTYPE html>
<html lang="en">
<head>
<meta charset="utf-8">
<title>DATAVEIL – GDPR discovery and classification of personal data</title>
<link rel="stylesheet" href="https://fonts.googleapis.com/css2?family=Oswald:wght@400;500&family=Poppins:wght@300;400;500;600&display=swap">
<style>
:root{
  --navy:#1f3b73;
  --ink:#2a3850;
  --muted:#6b7486;
  --teal:#1f8f8c;
  --teal-dark:#136a6c;
  --cyan:#2bb3c9;
  --blue:#1669e6;
  --blue-deep:#0f4fc2;
  --grey-bg:#efefef;
  --line:#e3e5ea;
  --white:#ffffff;
}
*{margin:0;padding:0;box-sizing:border-box}
html,body{width:1200px;height:2711px;overflow:hidden}
body{position:relative;background:var(--white);font-family:"Poppins",sans-serif;color:var(--ink)}
.abs{position:absolute}

/* header */
.site-header{top:0;left:0;width:1200px;height:83px;background:var(--white)}
.brand{left:85px;top:20px;display:flex;align-items:center;gap:10px;font-weight:600;font-size:30px;color:var(--navy);letter-spacing:1px}
.brand-dot{width:14px;height:14px;border-radius:50%;background:var(--cyan)}
.main-nav{right:85px;top:30px;display:flex;gap:66px;font-size:16px;color:var(--ink)}

/* hero */
.hero{top:83px;left:0;width:1200px;height:559px;background:linear-gradient(135deg,#22a39c 0%,var(--teal) 45%,var(--teal-dark) 100%)}
.hero-title{left:112px;top:183px;font-family:"Oswald",sans-serif;font-size:46px;letter-spacing:6px;color:var(--white);font-weight:400}
.hero-sub{left:112px;top:262px;font-family:"Oswald",sans-serif;font-size:32px;line-height:45px;color:var(--white);letter-spacing:1px;font-weight:400}
.hero-arrow{top:255px;width:18px;height:50px}
.hero-media{left:730px;top:110px;width:330px;height:340px}

/* section titles */
.section-title{left:0;width:1200px;text-align:center;font-size:25px;font-weight:400;color:var(--ink)}
.title-mark{left:577px;width:46px;height:8px}
.rule{left:0;width:1200px;height:1px;background:var(--line)}

/* features */
.features-art{left:0;top:777px;width:522px;height:428px;background:linear-gradient(160deg,#6fa3b9,#5a8fa8)}
.feature-list{left:551px;top:778px;width:620px;list-style:none}
.feature-list li{display:flex;align-items:center;gap:10px;font-size:15px;height:43px;color:var(--ink)}
.feature-list li.sub{font-size:13px;height:33px}
.feature-list li.sub small{font-size:10px;color:var(--muted)}
.f-icon{width:24px;height:22px;flex:none}
.s-icon{width:12px;height:12px;flex:none}

/* use cases */
.case{display:flex;align-items:center;gap:20px}
.case-box{width:68px;height:68px;background:var(--white);box-shadow:0 2px 10px rgba(30,50,90,.14);display:flex;align-items:center;justify-content:center;flex:none}
.case-text{font-size:13.5px;line-height:22px;color:var(--ink)}
.case-tags{display:flex;gap:22px;margin-top:6px;font-size:13px}
.case-tags span{display:flex;align-items:center;gap:5px}

/* highlights */
.accordion{left:87px;top:1812px;width:502px}
.acc-item{border-bottom:1px solid var(--line);padding:20px 0 22px 0;display:flex;gap:20px;font-size:16px;line-height:25px}
.acc-sign{width:14px;height:14px;border:1px solid #b9bfca;font-size:11px;line-height:12px;text-align:center;color:var(--muted);flex:none;margin-top:5px}
.acc-sub{list-style:none;margin-top:8px;font-size:13px;line-height:27px}
.acc-sub li::before{content:"»";color:var(--cyan);margin-right:8px}
.highlights-art{left:620px;top:1798px;width:580px;height:417px;background:linear-gradient(135deg,var(--blue),var(--blue-deep))}

/* contact */
.contact{top:2271px;left:0;width:1200px;height:337px;background:var(--grey-bg)}
.contact-form{left:87px;top:2271px;width:403px;height:340px;background:var(--white);box-shadow:0 4px 16px rgba(0,0,0,.08);padding:56px 26px 0}
.field{border-bottom:1px solid #d7dae0;font-size:12px;color:#8a90a0;padding-bottom:12px;margin-bottom:40px}
.btn{display:inline-block;background:var(--cyan);color:var(--white);font-size:14px;padding:10px 18px;border-radius:22px}
.contact-info{left:549px;top:2326px}
.contact-info h2{font-weight:400;font-size:27px;color:var(--ink)}
.contact-info .mark{margin:4px 0 20px}
.contact-info address{font-style:normal;font-size:13px;line-height:22px}
.contact-lines{display:flex;gap:36px;margin-top:22px;font-size:17px;align-items:center}
.contact-lines span{display:flex;align-items:center;gap:14px}
.round{width:40px;height:40px;border:1px solid var(--cyan);border-radius:50%;display:flex;align-items:center;justify-content:center}

/* footer */
.site-footer{top:2608px;left:0;width:1200px;height:103px;background:var(--navy);color:var(--white)}
.newsletter-title{left:85px;top:26px;font-size:19px;line-height:26px;font-weight:500}
.newsletter{left:277px;top:34px;display:flex;height:40px}
.newsletter .input{width:232px;border:1px solid #5a73a8;border-right:0;border-radius:22px 0 0 22px;font-size:12px;color:#b6c2dd;padding:11px 18px}
.newsletter .go{background:var(--cyan);border-radius:0 22px 22px 0;padding:10px 14px;font-size:15px}
.social{right:88px;top:30px;display:flex;gap:22px}
.social span{width:12px;height:12px;border-radius:50%;background:var(--white)}
.copyright{right:88px;top:70px;font-size:11px;color:#c8d2e8}
</style>
</head>
<body>

<header class="site-header abs">
  <div class="brand abs">DATAVEIL<span class="brand-dot"></span></div>
  <nav class="main-nav abs"><span>Home</span><span>Features</span><span>Use cases</span><span>Highlights</span><span>Contact</span></nav>
</header>

<section class="hero abs">
  <svg class="hero-arrow abs" style="left:16px" viewBox="0 0 18 50"><path d="M15 3 3 25l12 22" fill="none" stroke="#cfeeee" stroke-width="2"/></svg>
  <svg class="hero-arrow abs" style="right:16px" viewBox="0 0 18 50"><path d="M3 3l12 22L3 47" fill="none" stroke="#cfeeee" stroke-width="2"/></svg>
  <h1 class="hero-title abs">GDPR</h1>
  <p class="hero-sub abs">DISCOVERY AND CLASSIFICATION OF<br>PERSONAL DATA</p>
  <svg class="hero-media abs" viewBox="0 0 330 340" role="img" aria-label="Software product box shown inside a hexagon frame">
    <defs><linearGradient id="boxTone" x1="0" y1="0" x2="1" y2="1"><stop offset="0" stop-color="#ffffff"/><stop offset="1" stop-color="#dfe6ea"/></linearGradient></defs>
    <polygon points="82,4 248,4 328,170 248,336 82,336 2,170" fill="none" stroke="#3fd0cf" stroke-width="3"/>
    <polygon points="88,14 242,14 316,170 242,326 88,326 14,170" fill="url(#boxTone)"/>
  </svg>
</section>

<h2 class="section-title abs" style="top:690px">MAIN FEATURES</h2>
<svg class="title-mark abs" style="top:728px" viewBox="0 0 46 8"><circle cx="3" cy="4" r="1.5" fill="#2a3850"/><rect x="9" y="3" width="28" height="2" fill="#2a3850"/><circle cx="43" cy="4" r="1.5" fill="#2a3850"/></svg>

<div class="features-art abs" role="img" aria-label="Flat illustration of hands typing on a laptop with code on screen, notepad, glasses and coffee"></div>

<ul class="feature-list abs">
  <li><svg class="f-icon" viewBox="0 0 24 22"><rect x="1" y="2" width="22" height="18" rx="4" fill="none" stroke="#2bb3c9" stroke-width="2"/><circle cx="15" cy="13" r="4" fill="#2bb3c9"/></svg>Detection of personal and sensitive data for GDPR compliance</li>
  <li class="sub"><svg class="s-icon" viewBox="0 0 12 12"><circle cx="6" cy="6" r="6" fill="#2bb3c9"/><path d="M4.5 3.5 7 6 4.5 8.5" stroke="#fff" stroke-width="1.4" fill="none"/></svg><span>In structural sources <small>(e.g. SQL servers)</small></span></li>
  <li class="sub"><svg class="s-icon" viewBox="0 0 12 12"><circle cx="6" cy="6" r="6" fill="#2bb3c9"/><path d="M4.5 3.5 7 6 4.5 8.5" stroke="#fff" stroke-width="1.4" fill="none"/></svg><span>In unstructured sources <small>(e.g. documents, e-mails, logs, data streams)</small></span></li>
  <li class="sub"><svg class="s-icon" viewBox="0 0 12 12"><circle cx="6" cy="6" r="6" fill="#2bb3c9"/><path d="M4.5 3.5 7 6 4.5 8.5" stroke="#fff" stroke-width="1.4" fill="none"/></svg><span>In "noisy" content written in natural language <small>(e.g. containing errors or custom formats)</small></span></li>
  <li class="sub"><svg class="s-icon" viewBox="0 0 12 12"><circle cx="6" cy="6" r="6" fill="#2bb3c9"/><path d="M4.5 3.5 7 6 4.5 8.5" stroke="#fff" stroke-width="1.4" fill="none"/></svg><span>Built in ML models and rules for personal data used in Poland</span></li>
  <li><svg class="f-icon" viewBox="0 0 24 22"><rect x="1" y="2" width="22" height="18" rx="4" fill="none" stroke="#2bb3c9" stroke-width="2"/><circle cx="15" cy="13" r="4" fill="#2bb3c9"/></svg>Fast cataloging and classification of data and sources</li>
  <li><svg class="f-icon" viewBox="0 0 24 22"><rect x="1" y="2" width="22" height="18" rx="4" fill="none" stroke="#2bb3c9" stroke-width="2"/><circle cx="15" cy="13" r="4" fill="#2bb3c9"/></svg>Unified data registry for RODO compliance fulfilment</li>
  <li><svg class="f-icon" viewBox="0 0 24 22"><rect x="1" y="2" width="22" height="18" rx="4" fill="none" stroke="#2bb3c9" stroke-width="2"/><circle cx="15" cy="13" r="4" fill="#2bb3c9"/></svg>Management of consents and data access policies</li>
  <li><svg class="f-icon" viewBox="0 0 24 22"><rect x="1" y="2" width="22" height="18" rx="4" fill="none" stroke="#2bb3c9" stroke-width="2"/><circle cx="15" cy="13" r="4" fill="#2bb3c9"/></svg>Customizable analytics and reporting</li>
  <li><svg class="f-icon" viewBox="0 0 24 22"><rect x="1" y="2" width="22" height="18" rx="4" fill="none" stroke="#2bb3c9" stroke-width="2"/><circle cx="15" cy="13" r="4" fill="#2bb3c9"/></svg>Ability to integrates with tools for data anonymization or depersonalization</li>
  <li><svg class="f-icon" viewBox="0 0 24 22"><rect x="1" y="2" width="22" height="18" rx="4" fill="none" stroke="#2bb3c9" stroke-width="2"/><circle cx="15" cy="13" r="4" fill="#2bb3c9"/></svg>RESTful API for system management and integration</li>
</ul>

<div class="rule abs" style="top:1261px"></div>

<h2 class="section-title abs" style="top:1292px">USE CASES</h2>
<svg class="title-mark abs" style="top:1330px" viewBox="0 0 46 8"><circle cx="3" cy="4" r="1.5" fill="#2a3850"/><rect x="9" y="3" width="28" height="2" fill="#2a3850"/><circle cx="43" cy="4" r="1.5" fill="#2a3850"/></svg>

<div class="case abs" style="left:87px;top:1364px">
  <div class="case-box"><svg width="36" height="36" viewBox="0 0 36 36"><rect x="4" y="4" width="12" height="12" fill="#2bb3c9"/><rect x="20" y="4" width="12" height="12" fill="#2bb3c9"/><rect x="4" y="20" width="12" height="12" fill="#2bb3c9"/><rect x="20" y="20" width="12" height="12" fill="#2bb3c9"/></svg></div>
  <p class="case-text">Internal audits and verification of the current status - in<br>preparation for ensuring RODO compliance RODO</p>
</div>
<div class="case abs" style="left:614px;top:1364px">
  <div class="case-box"><svg width="36" height="36" viewBox="0 0 36 36" fill="none" stroke="#2bb3c9" stroke-width="2.4"><ellipse cx="18" cy="8" rx="13" ry="4"/><path d="M5 8v20c0 2 6 4 13 4s13-2 13-4V8M5 18c0 2 6 4 13 4s13-2 13-4"/></svg></div>
  <p class="case-text">Cataloging sources that store sensitive data</p>
</div>
<div class="case abs" style="left:87px;top:1464px">
  <div class="case-box"><svg width="36" height="36" viewBox="0 0 36 36" fill="none" stroke="#2bb3c9" stroke-width="2.6"><path d="M12 30V6M6 12l6-6 6 6M24 6v24M18 24l6 6 6-6"/></svg></div>
  <p class="case-text">Keeping the registry of personal data in order to implement<br>rights to information, forgetfulness,<br>data transfer</p>
</div>
<div class="case abs" style="left:614px;top:1464px">
  <div class="case-box"><svg width="36" height="36" viewBox="0 0 36 36"><rect x="5" y="5" width="26" height="26" rx="2" fill="#2bb3c9"/><rect x="11" y="5" width="14" height="9" fill="#fff"/><rect x="10" y="19" width="16" height="12" fill="#fff"/></svg></div>
  <p class="case-text">Continuous monitoring and classification of data</p>
</div>
<div class="case abs" style="left:87px;top:1560px;align-items:flex-start">
  <div class="case-box"><svg width="36" height="36" viewBox="0 0 36 36" fill="none" stroke="#2bb3c9" stroke-width="2.4"><path d="M18 4 33 32H3Z"/><path d="M10 20h16M7 26h22"/></svg></div>
  <div class="case-text" style="margin-top:6px">Use collected the data to create additional business value, e.g.:
    <div class="case-tags">
      <span><svg class="s-icon" viewBox="0 0 12 12"><circle cx="6" cy="6" r="6" fill="#2bb3c9"/><path d="M4.5 3.5 7 6 4.5 8.5" stroke="#fff" stroke-width="1.4" fill="none"/></svg>Classification of documents</span>
      <span><svg class="s-icon" viewBox="0 0 12 12"><circle cx="6" cy="6" r="6" fill="#2bb3c9"/><path d="M4.5 3.5 7 6 4.5 8.5" stroke="#fff" stroke-width="1.4" fill="none"/></svg>Analysis of sentiment</span>
      <span><svg class="s-icon" viewBox="0 0 12 12"><circle cx="6" cy="6" r="6" fill="#2bb3c9"/><path d="M4.5 3.5 7 6 4.5 8.5" stroke="#fff" stroke-width="1.4" fill="none"/></svg>Customer analytics for marketing</span>
      <span><svg class="s-icon" viewBox="0 0 12 12"><circle cx="6" cy="6" r="6" fill="#2bb3c9"/><path d="M4.5 3.5 7 6 4.5 8.5" stroke="#fff" stroke-width="1.4" fill="none"/></svg>Fraud detection</span>
      <span><svg class="s-icon" viewBox="0 0 12 12"><circle cx="6" cy="6" r="6" fill="#2bb3c9"/><path d="M4.5 3.5 7 6 4.5 8.5" stroke="#fff" stroke-width="1.4" fill="none"/></svg>Data governance</span>
    </div>
  </div>
</div>

<div class="rule abs" style="top:1680px"></div>

<h2 class="section-title abs" style="top:1720px">HIGHLIGHTS</h2>
<svg class="title-mark abs" style="top:1758px" viewBox="0 0 46 8"><circle cx="3" cy="4" r="1.5" fill="#2a3850"/><rect x="9" y="3" width="28" height="2" fill="#2a3850"/><circle cx="43" cy="4" r="1.5" fill="#2a3850"/></svg>

<div class="accordion abs">
  <div class="acc-item"><span class="acc-sign">+</span><div>Built in support for detection of Polish personal data</div></div>
  <div class="acc-item"><span class="acc-sign">+</span><div>High effectiveness of personal data detection<br>(also "noisy" data) by combining</div></div>
  <div class="acc-item"><span class="acc-sign">+</span><div>Supports structured and unstructured data source</div></div>
  <div class="acc-item" style="border-bottom:0"><span class="acc-sign">-</span><div>Ready for high performance processing
    <ul class="acc-sub"><li>Handles TBs of data easily</li><li>linear scalability</li><li>High availability and DRC deployments</li></ul></div></div>
</div>

<div class="highlights-art abs" role="img" aria-label="Flat illustration of devices and documents protected by a shield with a padlock"></div>

<section class="contact abs"></section>
<div class="contact-form abs">
  <div class="field">Your name</div>
  <div class="field">Email address</div>
  <div class="field">Phone number</div>
  <span class="btn">Send Message</span>
</div>
<div class="contact-info abs">
  <h2>Contact Us</h2>
  <svg class="mark" width="40" height="6" viewBox="0 0 40 6"><rect y="2" width="24" height="2" fill="#2a3850"/><circle cx="30" cy="3" r="1.5" fill="#2a3850"/><circle cx="36" cy="3" r="1.5" fill="#2a3850"/></svg>
  <address>Velmora Sp. z o.o.<br>ul. Lipowa 7<br>02-417 Warszawa</address>
  <div class="contact-lines">
    <span><span class="round"><svg width="18" height="18" viewBox="0 0 24 24"><path d="M6 2l4 4-2 3c1 3 4 6 7 7l3-2 4 4-3 4C10 22 2 14 2 5z" fill="#2bb3c9"/></svg></span>4800 555 210</span>
    <span><span class="round"><svg width="18" height="18" viewBox="0 0 24 24" fill="none" stroke="#2bb3c9" stroke-width="2"><rect x="3" y="6" width="18" height="13" rx="1"/><path d="M3 7l9 7 9-7"/></svg></span>hello@velmora.example</span>
  </div>
</div>

<footer class="site-footer abs">
  <div class="newsletter-title abs">Subscribe to Our<br>Newsletter</div>
  <div class="newsletter abs"><div class="input">Your email</div><div class="go">Subscribe</div></div>
  <div class="social abs"><span></span><span></span><span></span><span></span></div>
  <div class="copyright abs">Copyright © GDPR 2018. All Rights Reserved.</div>
</footer>

</body>
</html>
```